Belvant Systems Business Card

Utilize the newly designed logo to create a polished, professional 2-sided business card for this IT Services company.

Target Market(s)

IT Professionals many in the telecommunications and medical industries.

Industry/Entity Type

Business

Requirements
Must have
• Use of new logo, identified color palette and font: Albertus MT Std Regular.

```html
<!DOCTYPE html>
<html lang="en">
<head>
<meta charset="utf-8">
<title>Belvant Systems Business Card</title>
<link href="https://fonts.googleapis.com/css2?family=Marcellus&family=Open+Sans:wght@400&display=swap" rel="stylesheet">
<style>
  :root {
    --stage: #2b2b2b;
    --card-white: #ffffff;
    --card-shade: #e9e9ec;
    --indigo: #2a0c9c;
    --cyan: #1eb2df;
    --ink: #2a0c9c;
  }
  * { margin: 0; padding: 0; box-sizing: border-box; }
  html, body {
    width: 1200px;
    height: 900px;
    overflow: hidden;
    background: var(--stage);
  }
  .canvas {
    position: relative;
    width: 1200px;
    height: 900px;
  }
  .card {
    position: absolute;
    left: 250px;
    width: 700px;
    height: 400px;
    background: linear-gradient(135deg, var(--card-white) 0%, var(--card-white) 55%, var(--card-shade) 100%);
    box-shadow: 0 6px 18px rgba(0, 0, 0, 0.5);
    overflow: hidden;
  }
  .card--front { top: 35px; }
  .card--back { top: 465px; }

  .wordmark {
    font-family: "Marcellus", serif;
    font-weight: 400;
    color: var(--ink);
    line-height: 1;
    letter-spacing: 0.02em;
  }
  .wordmark__main { display: block; }
  .wordmark__sub { display: block; letter-spacing: 0.08em; }

  /* front */
  .front__disc {
    position: absolute;
    left: 70px;
    top: 100px;
    width: 200px;
    height: 200px;
    border-radius: 50%;
    background: var(--indigo);
  }
  .front__wordmark {
    position: absolute;
    left: 340px;
    top: 160px;
  }
  .front__wordmark .wordmark__main { font-size: 50px; }
  .front__wordmark .wordmark__sub { font-size: 25px; margin-top: 6px; padding-left: 28px; }

  /* back */
  .back__brand {
    position: absolute;
    right: 70px;
    top: 60px;
    display: flex;
    align-items: center;
    gap: 26px;
  }
  .back__disc {
    width: 86px;
    height: 86px;
    border-radius: 50%;
    background: var(--indigo);
  }
  .back__brand .wordmark__main { font-size: 40px; }
  .back__brand .wordmark__sub { font-size: 20px; margin-top: 4px; padding-left: 22px; }

  .contact {
    position: absolute;
    right: 70px;
    top: 195px;
    list-style: none;
    text-align: right;
    font-family: "Open Sans", sans-serif;
    font-size: 17px;
    line-height: 1.45;
    color: var(--ink);
  }
  .person {
    position: absolute;
    left: 60px;
    bottom: 50px;
    color: var(--ink);
  }
  .person__name {
    font-family: "Marcellus", serif;
    font-size: 30px;
    font-weight: 400;
    line-height: 1.1;
  }
  .person__role {
    font-family: "Open Sans", sans-serif;
    font-size: 18px;
    margin-top: 2px;
  }
</style>
</head>
<body>
<main class="canvas">
  <section class="card card--front" aria-label="Business card front">
    <div class="front__disc" aria-hidden="true"></div>
    <h1 class="wordmark front__wordmark">
      <span class="wordmark__main">BELVANT</span>
      <span class="wordmark__sub">SYSTEMS</span>
    </h1>
  </section>

  <section class="card card--back" aria-label="Business card back">
    <div class="back__brand">
      <div class="back__disc" aria-hidden="true"></div>
      <h2 class="wordmark">
        <span class="wordmark__main">BELVANT</span>
        <span class="wordmark__sub">SYSTEMS</span>
      </h2>
    </div>
    <ul class="contact">
      <li>4410 382 907</li>
      <li>dharrow@belvantsys.net</li>
      <li>www.belvantsys.net</li>
    </ul>
    <div class="person">
      <p class="person__name">Daniel Harrow</p>
      <p class="person__role">managing director</p>
    </div>
  </section>
</main>
</body>
</html>
```